Willowmere Haven tri-fold brochure

We are a small assisted living in a home-like environment. Brochure should be warm, heartfelt and include the list of services we provide (see existing brochure). I also want the front picture replaced with stock photo (so no picture of owners). New name to use (instead of Hester) is Dorian Feltrowe, and email is feltrowe@quintmail.example. Address is same. If you can find better photos, that would be good, all the photos here are dated. We are looking for a more professional design that still conveys warmth, because we are in a home-setting and only care for 9 residents.

Target Market(s)

35-55 year old children looking for an assisted living because their parents are unable to care for them.

Industry/Entity Type

Environment

Contact Information for Business Card

Dorian Feltrowe
Willowmere Haven or Willowmere Haven Assisted Living
40718 Pinegrove Ln. Conroe, TX 77519
281-647-5192

Requirements
Must have
• List of services offered (feel free to re-word or add/change)
• Be sure to change "Hester/Hestie" to Dorian / Dorian Feltrowe

```html
<!DOCTYPE html>
<html lang="en">
<head>
<meta charset="utf-8">
<title>Willowmere Haven – Brochure Outside Panels</title>
<link rel="stylesheet" href="https://fonts.googleapis.com/css2?family=Open+Sans:ital,wght@0,600;0,700;1,400;1,700&family=Yellowtail&display=block">
<style>
  :root {
    --navy: #2e3192;
    --orange: #f05a28;
    --white: #ffffff;
    --ink: #222222;
    --photo-warm: #d9c8bd;
    --photo-cool: #c7ccd6;
  }
  * { box-sizing: border-box; margin: 0; padding: 0; }
  html, body { width: 1200px; height: 927px; overflow: hidden; background: var(--white); }
  .brochure {
    position: relative; width: 1200px; height: 927px; overflow: hidden;
    background: var(--navy); font-family: "Open Sans", Arial, sans-serif; color: var(--white);
  }
  .backdrop { position: absolute; inset: 0; }
  .abs { position: absolute; }
  .script { font-family: "Yellowtail", "Brush Script MT", cursive; font-weight: 400; font-style: normal; }

  /* Left panel */
  .testimonials-title {
    left: 0; width: 395px; top: 232px; text-align: center;
    font-size: 36px; font-weight: 700; font-style: italic;
  }
  .quote-card {
    position: absolute; left: 57px; width: 308px; background: var(--white);
    border-radius: 6px; padding: 9px 16px; color: var(--ink);
    font-size: 15px; line-height: 24.5px; font-weight: 700; font-style: italic; text-align: justify;
  }
  .quote-card .script { color: var(--navy); font-size: 19px; line-height: 22px; }
  .quote-mark {
    position: absolute; left: 31px; font-size: 34px; font-weight: 700; color: var(--white); line-height: 1;
  }
  .references { left: 0; width: 395px; top: 846px; text-align: center; font-size: 18px; font-weight: 700; }

  /* Middle panel */
  .headline {
    left: 390px; width: 410px; top: 138px; text-align: center;
    font-size: 33px; line-height: 38px;
  }
  .promise {
    left: 390px; width: 400px; top: 354px; text-align: center;
    font-size: 36px; line-height: 46px;
  }
  .services {
    left: 440px; width: 310px; top: 610px; list-style: none;
    display: grid; grid-template-columns: 1fr 1fr; column-gap: 14px; row-gap: 4px;
    font-size: 14px; font-weight: 600; line-height: 20px;
  }
  .services li::before { content: "\2713"; margin-right: 6px; font-weight: 700; }
  .invite {
    left: 390px; width: 410px; top: 782px; text-align: center;
    font-size: 17.5px; line-height: 26px; font-style: italic;
  }
  .address {
    left: 390px; width: 410px; top: 846px; text-align: center;
    font-size: 17px; line-height: 23px; font-weight: 700;
  }

  /* Right panel */
  .brand-name {
    left: 800px; width: 400px; top: 170px; text-align: center; white-space: nowrap;
    font-size: 40px; font-weight: 700; letter-spacing: -0.5px;
  }
  .brand-tagline {
    left: 810px; width: 380px; top: 288px; text-align: center;
    font-size: 18px; font-weight: 700;
  }
  .commitment {
    left: 860px; width: 280px; top: 710px; text-align: center;
    font-size: 17.5px; line-height: 26px; font-style: italic;
  }
  .divider { left: 895px; width: 210px; top: 824px; height: 2px; background: linear-gradient(90deg, transparent, var(--white), transparent); }
  .contact-name { left: 860px; width: 280px; top: 834px; text-align: center; font-size: 20px; font-weight: 700; }
  .contact-phone { left: 840px; width: 320px; top: 860px; text-align: center; font-size: 37px; font-weight: 700; }
</style>
</head>
<body>
<main class="brochure">
  <svg class="backdrop" width="1200" height="927" viewBox="0 0 1200 927" aria-hidden="true">
    <path d="M0,140 C170,100 340,60 480,0 L1200,0 L1200,300 C1110,470 960,640 780,705 C640,755 520,768 380,770 C250,770 110,730 0,680 Z" fill="var(--orange)"/>
    <path d="M0,140 C170,100 340,60 480,0" fill="none" stroke="var(--white)" stroke-width="7"/>
    <path d="M0,130 C170,90 330,52 470,0" fill="none" stroke="var(--white)" stroke-width="2" opacity=".6"/>
    <path d="M380,776 C520,774 650,760 790,712 C970,648 1110,480 1200,310" fill="none" stroke="var(--white)" stroke-width="8"/>
    <rect x="22" y="560" width="353" height="246" rx="22" fill="var(--orange)"/>
    <circle cx="1000" cy="542" r="162" fill="var(--white)"/>
    <path d="M845,560 A156,156 0 0 1 1100,420" fill="none" stroke="var(--orange)" stroke-width="8"/>
    <path d="M1150,500 A156,156 0 0 1 1080,685" fill="none" stroke="var(--navy)" stroke-width="8"/>
    <circle cx="197" cy="145" r="65" fill="var(--white)"/>
  </svg>

  <div class="abs" role="img" aria-label="Photo of smiling senior residents giving a thumbs up"
       style="left:138px;top:86px;width:118px;height:118px;border-radius:50%;background:radial-gradient(circle at 45% 40%, var(--photo-warm), #b99f92);"></div>
  <div class="abs" role="img" aria-label="Portrait photo of a smiling senior woman resting her cheek on her hand"
       style="left:856px;top:398px;width:288px;height:288px;border-radius:50%;background:radial-gradient(circle at 40% 40%, #efe8e3, var(--photo-cool));"></div>

  <h2 class="abs testimonials-title">Testimonials</h2>

  <span class="quote-mark" style="top:300px">&ldquo;</span>
  <blockquote class="quote-card" style="top:305px">My mom lived in five private care homes. When she moved here she said: "<span class="script">I've finally found my home!</span>"</blockquote>

  <span class="quote-mark" style="top:428px">&ldquo;</span>
  <blockquote class="quote-card" style="top:433px">"I lived in a facility where everything seemed to be... door..., door..., door... <span class="script">Here is small, familiar and comfortable</span>"</blockquote>

  <span class="quote-mark" style="top:572px">&ldquo;</span>
  <blockquote class="quote-card" style="top:577px;text-align:left">"<span class="script">I'd be miserable in a nursing home!</span>" If you are one of the millions of people who feel this way, we say, "<span class="script">Trust your instincts</span>" Discover that smaller is better where full service care is provided in a real home.</blockquote>

  <p class="abs references">References Available</p>

  <p class="abs script headline">Smaller is better<br>when it comes to the elderly</p>
  <p class="abs script promise">Our unique homes<br>are designed to<br>make the surroundings<br>familiar and the<br>care consistent.</p>
  <ul class="abs services" aria-label="Services">
    <li>Home-cooked meals</li>
    <li>Medication help</li>
    <li>Bathing &amp; dressing</li>
    <li>Memory care</li>
    <li>Housekeeping</li>
    <li>24-hour staff</li>
  </ul>
  <p class="abs invite">Please call for a personal tour and<br>experience the willowmere haven difference.</p>
  <p class="abs address">40718 Pinegrove Ln. Conroe, Texas.<br>feltrowe@quintmail.example</p>

  <h1 class="abs brand-name">Willowmere Haven</h1>
  <p class="abs brand-tagline">Assisted Living &amp; Memory Care</p>
  <p class="abs commitment">Offering a true and noble<br>commitment to the<br>highest standards of care<br>in the industry.</p>
  <div class="abs divider"></div>
  <p class="abs contact-name">Dorian Feltrowe</p>
  <p class="abs contact-phone">281-647-5192</p>
</main>
</body>
</html>
```